RivoPlex PowerPoint Template with existing Logo and Letterhead template

Develop a PowerPoint template based on existing logo and letterhead designs for a Marketing Consultancy.
Presentations that will be made with title slide, content slides (which includes mostly bullet point text and some tables) and also last page company introduction and copyright.
Corporate colors should be keep as per the logo

I like something like from Artisan Hive
- Serious, Modern PowerPoint Design for Company in Canada | Design 418674
- Professional, Modern PowerPoint Design for Company in United States | Design 7795293
- Professional, Modern PowerPoint Design for Company in United States | Design 7826742
- Serious, Modern PowerPoint Design for Company in Canada | Design 418635
- Elegant, Serious PowerPoint Design for Company in Puerto Rico | Design 16951178
- Bold, Modern PowerPoint Design for Company in United States | Design 11745238

To all designers, • We need sleek and modern looking PowerPoint presentation template. • The template will primarily be used for our corporate slide and solutions presentation for our customers. • Not too much of white and it should be sleek, modern and impressive for marketing consultancy firms like us. • Please ensure the content pages are water marketed with the 4 boxes. • I like something like from Artisan Hive and you can get some idea on what I like.: o Serious, Modern PowerPoint Design for Company in Canada | Design 418674 o Professional, Modern PowerPoint Design for Company in United States | Design 7795293 o Professional, Modern PowerPoint Design for Company in United States | Design 7826742 o Serious, Modern PowerPoint Design for Company in Canada | Design 418635 o Elegant, Serious PowerPoint Design for Company in Puerto Rico | Design 16951178 o Bold, Modern PowerPoint Design for Company in United States | Design 11745238 Thanks!

Target Market(s)

Marketing Managers, B2B Marketing Team, CRM Data Owners

Industry/Entity Type

Marketing

Requirements
Must have
• Not too much of white and it should be sleek, modern and impressive for marketing consultancy firms like us. Please ensure the content pages are water marketed with the 4 boxes. The template will primarily be used for our corporate slides and solutions presentation for our customers.
Should not have
• no background in the slide content area

```html
<!DOCTYPE html>
<html lang="en">
<head>
<meta charset="utf-8">
<title>RivoPlex Presentation Template</title>
<link href="https://fonts.googleapis.com/css2?family=Roboto+Condensed:wght@400;700&family=Open+Sans:ital,wght@0,400;0,600;1,400&display=swap" rel="stylesheet">
<style>
:root{
  --red:#e8202a;
  --red-soft:#f04a4f;
  --dark:#333335;
  --ink:#3d3d3f;
  --grey-bg:#9d9d9d;
  --white:#ffffff;
  --row:#dfe1ea;
  --gold:#a08a00;
}
*{margin:0;padding:0;box-sizing:border-box}
html,body{width:1200px;height:960px;overflow:hidden}
body{background:var(--grey-bg);position:relative;font-family:"Open Sans",sans-serif;color:var(--ink)}
.slide{position:absolute;width:381px;height:214px;background:var(--white);overflow:hidden}
.c1{left:16px}.c2{left:410px}.c3{left:803px}
.r1{top:37px}.r2{top:262px}.r3{top:486px}.r4{top:710px}
.slide-title{position:absolute;left:15px;top:13px;padding-left:9px;border-left:3px solid var(--red);font:700 15px/19px "Roboto Condensed",sans-serif;color:var(--dark)}
.brand{position:absolute;right:22px;top:17px;font:700 11px/12px "Roboto Condensed",sans-serif;color:var(--red);letter-spacing:1px;display:flex;align-items:center;gap:3px}
.brand .dot{width:5px;height:5px;background:var(--red)}
.footer{position:absolute;left:0;bottom:0;width:381px;height:52px}
.url{position:absolute;right:20px;bottom:6px;font-size:6.5px;color:var(--white)}
.tiny{font-size:4.6px;line-height:6.4px;color:var(--ink)}
.squares span{position:absolute;background:var(--red-soft);opacity:.85}

/* title slide */
.title-brand{position:absolute;left:22px;top:37px;font:700 22px/24px "Roboto Condensed",sans-serif;color:var(--red);letter-spacing:2px;display:flex;align-items:center;gap:5px}
.title-brand .dot{width:9px;height:9px;background:var(--red)}
.deck-title{position:absolute;left:21px;top:125px;font:400 22px/24px "Roboto Condensed",sans-serif;color:var(--white)}
.deck-sub{position:absolute;left:22px;top:150px;font:400 10px/12px "Roboto Condensed",sans-serif;color:var(--white)}

/* agenda */
.agenda-item{position:absolute;display:flex;align-items:center;gap:10px;font-size:7.5px;color:#666}
.agenda-item b{display:block;width:28px;height:17px;background:var(--dark);color:var(--white);font:400 10px/17px "Roboto Condensed",sans-serif;text-align:center}

/* about */
.mission{position:absolute;left:14px;right:14px;top:40px;font-style:italic;font-size:6.6px;line-height:9px;color:var(--red);text-align:center}
.about-text{position:absolute;left:17px;top:62px;width:190px}
.about-text p{margin-bottom:4px}
.about-text em{font-style:normal;color:var(--red)}
.photo{position:absolute;background:linear-gradient(135deg,#cfd6dc,#7e8b96)}

/* team */
.member{position:absolute;top:39px;width:78px;text-align:center}
.member .portrait{width:40px;height:40px;margin:0 auto;background:linear-gradient(160deg,#d8d8d8,#8a8a8a)}
.member .name{margin-top:11px;font-size:8.5px;line-height:9px;color:var(--red)}
.member .role{font-size:6px;line-height:8px;color:#555}
.member .tiny{margin-top:7px}
.member .tiny+.tiny{margin-top:4px}

/* two column */
.col{position:absolute;top:46px;width:168px}
.col p{margin-bottom:5px}

/* image with text */
.heading{position:absolute;left:10px;top:142px;font-size:8.5px;color:var(--red)}
.img-text{position:absolute;left:10px;top:152px;width:362px}

/* section divider */
.divider-brand{position:absolute;left:18px;top:29px;font:700 11px/12px "Roboto Condensed",sans-serif;color:var(--red);letter-spacing:1px;display:flex;align-items:center;gap:3px}
.divider-brand .dot{width:5px;height:5px;background:var(--red)}
.divider-rule{position:absolute;left:108px;top:21px;width:1px;height:32px;background:var(--red)}
.divider-title{position:absolute;left:116px;top:27px;font:400 14px/18px "Roboto Condensed",sans-serif;color:var(--dark)}
.divider-band{position:absolute;left:0;top:82px;width:328px;height:53px;background:var(--dark)}
.divider-band p{position:absolute;left:80px;top:10px;width:190px;font-size:5.4px;line-height:7.6px;color:#ddd}
.divider-go{position:absolute;left:328px;top:82px;width:53px;height:53px;background:var(--red)}

/* icons */
.feature{position:absolute;width:78px;text-align:center}
.feature svg{display:block;margin:0 auto;width:22px;height:22px}
.feature h4{margin-top:3px;font-size:5.6px;font-weight:600;color:var(--red)}
.feature h4.dark{color:var(--dark)}
.feature p{font-size:4.8px;line-height:6.2px;color:#aaa}

/* table */
.intro{position:absolute;left:45px;top:40px;width:300px;font-size:5.6px;line-height:7.6px;color:var(--dark)}
.data-table{position:absolute;left:61px;top:58px;width:253px;border-collapse:separate;border-spacing:1px;font-size:5px;color:var(--dark)}
.data-table th{background:var(--red);color:var(--white);font-weight:400;height:10px}
.data-table td{height:11px;text-align:center;background:var(--white)}
.data-table tbody tr:nth-child(odd) td{background:var(--row)}
.data-table td.phase{background:var(--dark)!important;color:var(--white);text-align:left;padding-left:3px;width:36px}
.outro{position:absolute;left:48px;top:155px;font-size:5.6px;line-height:7px;color:var(--dark)}

/* graphs */
.chart-intro{position:absolute;left:30px;top:36px;width:340px;font-size:6px;line-height:8px;color:var(--dark)}
.chart{position:absolute;left:20px;top:55px;width:350px;height:108px}
.chart-outro{position:absolute;left:33px;top:163px;font-size:6px;line-height:7px;color:var(--dark)}

/* contact & closing */
.contact-head{position:absolute;left:21px;top:113px;font:700 12px/14px "Roboto Condensed",sans-serif;color:var(--white)}
.contact-lines{position:absolute;left:21px;top:134px;font:400 8.2px/11px "Roboto Condensed",sans-serif;color:#ffe0e0}
.contact-lines li{list-style:none;display:flex;align-items:center;gap:6px}
.contact-lines li.gap{margin-top:4px}
.contact-lines svg{width:8px;height:8px}
.thanks{position:absolute;left:30px;top:88px;font:700 31px/34px "Roboto Condensed",sans-serif;color:var(--white)}
</style>
</head>
<body>

<!-- 1 Title -->
<section class="slide c1 r1">
  <div class="title-brand">RIVOPLEX<span class="dot"></span></div>
  <svg class="footer" style="height:214px;top:0" viewBox="0 0 381 214" preserveAspectRatio="none">
    <path d="M0 84 Q190 72 381 92 L381 100 Q190 82 0 94 Z" fill="#333335"/>
    <path d="M0 98 Q190 86 381 104 L381 214 L0 214 Z" fill="#e8202a"/>
  </svg>
  <div class="squares"><span style="left:307px;top:97px;width:24px;height:24px"></span><span style="left:343px;top:121px;width:26px;height:26px"></span><span style="left:334px;top:163px;width:47px;height:47px"></span></div>
  <h1 class="deck-title">PRESENTATION TITLE</h1>
  <p class="deck-sub">Place Title detail or Description here</p>
  <span class="url">www.rivoplex.com</span>
</section>

<!-- 2 Agenda -->
<section class="slide c2 r1">
  <h2 class="slide-title">Agenda</h2>
  <div class="brand">RIVOPLEX<span class="dot"></span></div>
  <div class="agenda-item" style="left:66px;top:41px"><b>01</b>Introduction</div>
  <div class="agenda-item" style="left:66px;top:69px"><b>02</b>About Us</div>
  <div class="agenda-item" style="left:66px;top:98px"><b>03</b>Our Team</div>
  <div class="agenda-item" style="left:66px;top:127px"><b>04</b>Services</div>
  <div class="agenda-item" style="left:66px;top:156px"><b>05</b>Solutions</div>
  <div class="agenda-item" style="left:225px;top:41px"><b>06</b>Portfolio</div>
  <div class="agenda-item" style="left:225px;top:69px"><b>07</b>Pricing</div>
  <div class="agenda-item" style="left:225px;top:98px"><b>08</b>Financial Data</div>
  <div class="agenda-item" style="left:225px;top:127px"><b>09</b>Testimonial</div>
  <div class="agenda-item" style="left:225px;top:156px"><b>10</b>Contact Us</div>
  <svg class="footer" viewBox="0 0 381 52" preserveAspectRatio="none"><path d="M0 24 Q190 10 381 14 L381 22 Q190 18 0 32 Z" fill="#333335"/><path d="M0 36 Q190 22 381 26 L381 52 L0 52 Z" fill="#e8202a"/></svg>
  <span class="url">www.rivoplex.com &nbsp;|&nbsp; 2</span>
</section>

<!-- 3 About Us -->
<section class="slide c3 r1">
  <h2 class="slide-title">About Us</h2>
  <div class="brand">RIVOPLEX<span class="dot"></span></div>
  <p class="mission">The mission of RivoPlex is to inspire growth companies to capture opportunities in billion dollar markets by inventing the future.</p>
  <div class="about-text tiny">
    <p>We help you achieve the next level of growth, productivity and profitability. Are you anticipating what's going to happen over the next five years? Are you connected to sources of innovation? More importantly, are your competitors?</p>
    <p>Internet of Things, Big Data and Analytics, 3D Printing, and more ... We have the expertise to help Business Leaders discover what's possible, identify exceptional opportunities, and create value in the New IoT Economy.</p>
    <p><em>Innovation is not mystical.</em> Innovation is methodical and planned. Innovation is necessary. Getting involved in the startup and VC ecosystem is an important step. We can show you how.</p>
    <p><em>Innovation is created</em> by strategically connecting marketplace trends with specific project planning. Innovation has developed business-driven innovation for anticipating future realities, identifying innovation, and accessing new revenue.</p>
  </div>
  <div class="photo" role="img" aria-label="Photo of business people meeting in a bright office" style="left:210px;top:69px;width:156px;height:102px"></div>
  <svg class="footer" viewBox="0 0 381 52" preserveAspectRatio="none"><path d="M0 24 Q190 10 381 14 L381 22 Q190 18 0 32 Z" fill="#333335"/><path d="M0 36 Q190 22 381 26 L381 52 L0 52 Z" fill="#e8202a"/></svg>
  <span class="url">www.rivoplex.com &nbsp;|&nbsp; 3</span>
</section>

<!-- 4 Our Team -->
<section class="slide c1 r2">
  <h2 class="slide-title">Our Team</h2>
  <div class="brand">RIVOPLEX<span class="dot"></span></div>
  <div class="member" style="left:26px"><div class="portrait" role="img" aria-label="Team member portrait"></div><p class="name">John Doe</p><p class="role">Manager</p><p class="tiny">Lorem ipsum dolor sit amet consectetur adipiscing elit. Vestibulum nec eros in dolor posuere interdum.</p><p class="tiny">Lorem ipsum dolor sit amet consectetur adipiscing elit. Vestibulum nec eros in dolor posuere interdum.</p></div>
  <div class="member" style="left:111px"><div class="portrait" role="img" aria-label="Team member portrait"></div><p class="name">John Doe</p><p class="role">Manager</p><p class="tiny">Lorem ipsum dolor sit amet consectetur adipiscing elit. Vestibulum nec eros in dolor posuere interdum.</p><p class="tiny">Lorem ipsum dolor sit amet consectetur adipiscing elit. Vestibulum nec eros in dolor posuere interdum.</p></div>
  <div class="member" style="left:189px"><div class="portrait" role="img" aria-label="Team member portrait"></div><p class="name">John Doe</p><p class="role">Manager</p><p class="tiny">Lorem ipsum dolor sit amet consectetur adipiscing elit. Vestibulum nec eros in dolor posuere interdum.</p><p class="tiny">Lorem ipsum dolor sit amet consectetur adipiscing elit. Vestibulum nec eros in dolor posuere interdum.</p></div>
  <div class="member" style="left:268px"><div class="portrait" role="img" aria-label="Team member portrait"></div><p class="name">John Doe</p><p class="role">Manager</p><p class="tiny">Lorem ipsum dolor sit amet consectetur adipiscing elit. Vestibulum nec eros in dolor posuere interdum.</p><p class="tiny">Lorem ipsum dolor sit amet consectetur adipiscing elit. Vestibulum nec eros in dolor posuere interdum.</p></div>
  <svg class="footer" viewBox="0 0 381 52" preserveAspectRatio="none"><path d="M0 24 Q190 10 381 14 L381 22 Q190 18 0 32 Z" fill="#333335"/><path d="M0 36 Q190 22 381 26 L381 52 L0 52 Z" fill="#e8202a"/></svg>
  <span class="url">www.rivoplex.com &nbsp;|&nbsp; 4</span>
</section>

<!-- 5 Two Column -->
<section class="slide c2 r2">
  <h2 class="slide-title">Two Column</h2>
  <div class="brand">RIVOPLEX<span class="dot"></span></div>
  <div class="col tiny" style="left:14px">
    <p>There are many variations of passages of Lorem Ipsum available, but the majority have suffered alteration in some form, by injected humour, or randomized words which don't look even slightly believable. If you are going to use a passage of Lorem Ipsum, you need to be sure there isn't anything embarrassing hidden in the middle of text. All the Lorem Ipsum generators.</p>
    <p>If you are going to use a passage of Lorem Ipsum, you need to be sure there isn't anything embarrassing hidden in the middle of text. All the Lorem Ipsum generators on the Internet tend to repeat predefined chunks as necessary, making this the first true generator on the Internet.</p>
    <p>It uses a dictionary of over 200 Latin words, combined with a handful of model sentence structures, to generate Lorem Ipsum which looks reasonable. The generated Lorem Ipsum is therefore always free from repetition, injected humour, or non-characteristic words etc.</p>
  </div>
  <div class="col tiny" style="left:199px">
    <p>There are many variations of passages of Lorem Ipsum available, but the majority have suffered alteration in some form, by injected humour, or randomized words which don't look even slightly believable. If you are going to use a passage of Lorem Ipsum, you need to be sure there isn't anything embarrassing hidden in the middle of text. All the Lorem Ipsum generators.</p>
    <p>If you are going to use a passage of Lorem Ipsum, you need to be sure there isn't anything embarrassing hidden in the middle of text. All the Lorem Ipsum generators on the Internet tend to repeat predefined chunks as necessary, making this the first true generator on the Internet.</p>
    <p>It uses a dictionary of over 200 Latin words, combined with a handful of model sentence structures, to generate Lorem Ipsum which looks reasonable. The generated Lorem Ipsum is therefore always free from repetition, injected humour, or non-characteristic words etc.</p>
  </div>
  <svg class="footer" viewBox="0 0 381 52" preserveAspectRatio="none"><path d="M0 24 Q190 10 381 14 L381 22 Q190 18 0 32 Z" fill="#333335"/><path d="M0 36 Q190 22 381 26 L381 52 L0 52 Z" fill="#e8202a"/></svg>
  <span class="url">www.rivoplex.com &nbsp;|&nbsp; 5</span>
</section>

<!-- 6 Image With Text -->
<section class="slide c3 r2">
  <h2 class="slide-title">Image With Text</h2>
  <div class="brand">RIVOPLEX<span class="dot"></span></div>
  <div class="photo" role="img" aria-label="Photo of hands writing in a notebook beside a tablet and glasses on a wooden table" style="left:0;top:38px;width:381px;height:98px;background:linear-gradient(120deg,#6b4a2f,#b89270 50%,#d9d2c6)"></div>
  <p class="heading">Heading</p>
  <p class="img-text tiny">There are many variations of passages of lorem ipsum available, but the majority have suffered alteration in some form, by injected humour, or randomized words which don't look even slightly believable. If you are going to use a passage of lorem ipsum, you need to be sure there isn't anything embarrassing hidden in the middle of text. All the lorem ipsum generators.</p>
  <svg class="footer" viewBox="0 0 381 52" preserveAspectRatio="none"><path d="M0 24 Q190 10 381 14 L381 22 Q190 18 0 32 Z" fill="#333335"/><path d="M0 36 Q190 22 381 26 L381 52 L0 52 Z" fill="#e8202a"/></svg>
  <span class="url">www.rivoplex.com &nbsp;|&nbsp; 6</span>
</section>

<!-- 7 Section Divider -->
<section class="slide c1 r3">
  <div class="divider-brand">RIVOPLEX<span class="dot"></span></div>
  <div class="divider-rule"></div>
  <h2 class="divider-title">Section Divider</h2>
  <div class="divider-band"><p>Lorem ipsum dolor sit amet, consectetur adipiscing elit. Vestibulum nec eros in dolor posuere interdum. Ut elementum, justo vel pretium condimentum, ante metus sodales nisi, eu aliquet</p></div>
  <div class="divider-go"><svg viewBox="0 0 53 53" width="53" height="53"><circle cx="26.5" cy="26.5" r="15" fill="none" stroke="#fff" stroke-width="1.6"/><path d="M19 26.5 H33 M28 21.5 L33 26.5 L28 31.5" fill="none" stroke="#fff" stroke-width="1.6"/></svg></div>
</section>

<!-- 8 Iconic -->
<section class="slide c2 r3">
  <h2 class="slide-title">Iconic</h2>
  <div class="brand">RIVOPLEX<span class="dot"></span></div>
  <div class="feature" style="left:23px;top:41px"><svg viewBox="0 0 24 24"><rect x="3" y="2" width="9" height="15" rx="1.5" fill="none" stroke="#e8202a" stroke-width="1.5"/><rect x="12" y="8" width="8" height="14" rx="1.5" fill="#fff" stroke="#e8202a" stroke-width="1.5"/></svg><h4>Relationship</h4><p>Nullam eu tempor purus. Nunc a leo magna, consequat risus. Nullam eu.</p></div>
  <div class="feature" style="left:108px;top:41px"><svg viewBox="0 0 24 24"><rect x="9" y="2" width="12" height="12" fill="#e8202a"/><rect x="6" y="6" width="12" height="12" fill="#c8161f" stroke="#fff" stroke-width="1"/><rect x="3" y="10" width="12" height="12" fill="#e8202a" stroke="#fff" stroke-width="1"/></svg><h4>Double Data</h4><p>Nullam eu tempor purus. Nunc a leo magna, consequat risus. Nullam eu.</p></div>
  <div class="feature" style="left:194px;top:41px"><svg viewBox="0 0 24 24"><circle cx="12" cy="13" r="9" fill="none" stroke="#e8202a" stroke-width="2"/><path d="M12 8 V13 H16" fill="none" stroke="#e8202a" stroke-width="1.6"/><path d="M2 6 L6 2 M22 6 L18 2" stroke="#e8202a" stroke-width="2"/></svg><h4>Time Up</h4><p>Nullam eu tempor purus. Nunc a leo magna, consequat risus. Nullam eu.</p></div>
  <div class="feature" style="left:279px;top:41px"><svg viewBox="0 0 24 24"><path d="M15 1 L5 14 H11 L8 23 L19 9 H13 Z" fill="#e8202a"/></svg><h4>Fast Response</h4><p>Nullam eu tempor purus. Nunc a leo magna, consequat risus. Nullam eu.</p></div>
  <div class="feature" style="left:23px;top:106px"><svg viewBox="0 0 24 24"><path d="M4 4 L20 20 M20 4 L4 20" stroke="#333335" stroke-width="3"/><circle cx="5" cy="5" r="3" fill="#333335"/></svg><h4 class="dark">Responsive</h4><p>Nullam eu tempor purus. Nunc a leo magna, consequat risus. Nullam eu.</p></div>
  <div class="feature" style="left:108px;top:106px"><svg viewBox="0 0 24 24"><rect x="9" y="1" width="6" height="10" fill="none" stroke="#333335" stroke-width="1.6"/><circle cx="12" cy="16" r="6" fill="none" stroke="#333335" stroke-width="1.8"/><circle cx="12" cy="16" r="2.2" fill="#333335"/></svg><h4 class="dark">Award</h4><p>Nullam eu tempor purus. Nunc a leo magna, consequat risus. Nullam eu.</p></div>
  <div class="feature" style="left:194px;top:106px"><svg viewBox="0 0 24 24"><rect x="5" y="2" width="14" height="20" rx="2" fill="none" stroke="#333335" stroke-width="1.8"/><rect x="7.5" y="5" width="9" height="12" fill="#fff" stroke="#333335" stroke-width=".8"/></svg><h4 class="dark">Digitalization</h4><p>Nullam eu tempor purus. Nunc a leo magna, consequat risus. Nullam eu.</p></div>
  <div class="feature" style="left:279px;top:106px"><svg viewBox="0 0 24 24"><path d="M12 2 V22" stroke="#333335" stroke-width="2"/><path d="M3 5 H19 L22 8 L19 11 H3 Z M5 13 H21 V18 H5 L2 15.5 Z" fill="#333335"/></svg><h4 class="dark">Mapping</h4><p>Nullam eu tempor purus. Nunc a leo magna, consequat risus. Nullam eu.</p></div>
  <svg class="footer" viewBox="0 0 381 52" preserveAspectRatio="none"><path d="M0 24 Q190 10 381 14 L381 22 Q190 18 0 32 Z" fill="#333335"/><path d="M0 36 Q190 22 381 26 L381 52 L0 52 Z" fill="#e8202a"/></svg>
  <span class="url">www.rivoplex.com &nbsp;|&nbsp; 7</span>
</section>

<!-- 9 Table -->
<section class="slide c3 r3">
  <h2 class="slide-title">Table</h2>
  <div class="brand">RIVOPLEX<span class="dot"></span></div>
  <p class="intro">Lorem ipsum dolor sit amet, consectetur adipiscing elit. Vestibulum nec eros in dolor posuere interdum. Ut elementum, justo vel pretium condimentum.</p>
  <table class="data-table">
    <thead><tr><th></th><th>JAN</th><th>FEB</th><th>MAR</th><th>APR</th><th>MAY</th><th>JUN</th></tr></thead>
    <tbody>
      <tr><td class="phase">Phase1</td><td>xx</td><td>xx</td><td>xx</td><td>xx</td><td>xx</td><td>xx</td></tr>
      <tr><td class="phase">Phase1</td><td>xx</td><td>xx</td><td>xx</td><td>xx</td><td>xx</td><td>xx</td></tr>
      <tr><td class="phase">Phase1</td><td>xx</td><td>xx</td><td>xx</td><td>xx</td><td>xx</td><td>xx</td></tr>
      <tr><td class="phase">Phase1</td><td>xx</td><td>xx</td><td>xx</td><td>xx</td><td>xx</td><td>xx</td></tr>
      <tr><td class="phase">Phase1</td><td>xx</td><td>xx</td><td>xx</td><td>xx</td><td>xx</td><td>xx</td></tr>
      <tr><td class="phase">Phase1</td><td>xx</td><td>xx</td><td>xx</td><td>xx</td><td>xx</td><td>xx</td></tr>
      <tr><td class="phase">Phase1</td><td>xx</td><td>xx</td><td>xx</td><td>xx</td><td>xx</td><td>xx</td></tr>
    </tbody>
  </table>
  <p class="outro">Lorem ipsum dolor sit amet, consectetur adipiscing elit. Vestibulum nec eros in dolor posuere interdum</p>
  <svg class="footer" viewBox="0 0 381 52" preserveAspectRatio="none"><path d="M0 24 Q190 10 381 14 L381 22 Q190 18 0 32 Z" fill="#333335"/><path d="M0 36 Q190 22 381 26 L381 52 L0 52 Z" fill="#e8202a"/></svg>
  <span class="url">www.rivoplex.com &nbsp;|&nbsp; 8</span>
</section>

<!-- 10 Graphs -->
<section class="slide c1 r4">
  <h2 class="slide-title">Graphs</h2>
  <div class="brand">RIVOPLEX<span class="dot"></span></div>
  <p class="chart-intro">Lorem ipsum dolor sit amet, consectetur adipiscing elit. Vestibulum nec eros in dolor posuere interdum. Ut elementum, justo vel pretium condimentum,</p>
  <svg class="chart" viewBox="0 0 350 108" font-family="Open Sans, sans-serif">
    <g font-size="5.5" fill="#e8202a" text-anchor="end">
      <text x="13" y="98">0</text><text x="13" y="84">1</text><text x="13" y="70">2</text><text x="13" y="56">3</text><text x="13" y="42">4</text><text x="13" y="28">5</text><text x="13" y="14">6</text>
    </g>
    <path d="M18 12 V96 H350" fill="none" stroke="#a08a00" stroke-width=".8"/>
    <g>
      <rect x="34" y="35.8" width="17" height="60.2" fill="#a08a00"/><rect x="51" y="62.4" width="17" height="33.6" fill="#111"/><rect x="68" y="68" width="17" height="28" fill="#e8202a"/>
      <rect x="112" y="61" width="17" height="35" fill="#a08a00"/><rect x="129" y="34.4" width="17" height="61.6" fill="#111"/><rect x="146" y="68" width="17" height="28" fill="#e8202a"/>
      <rect x="189" y="47" width="17" height="49" fill="#a08a00"/><rect x="206" y="70.8" width="17" height="25.2" fill="#111"/><rect x="223" y="54" width="17" height="42" fill="#e8202a"/>
      <rect x="267" y="33" width="17" height="63" fill="#a08a00"/><rect x="284" y="56.8" width="17" height="39.2" fill="#111"/><rect x="301" y="26" width="17" height="70" fill="#e8202a"/>
    </g>
    <path d="M200 0 H240 V20 H224 L220 25 L216 20 H200 Z" fill="#e8202a"/>
    <text x="220" y="14" font-size="9" fill="#fff" text-anchor="middle">87%</text>
    <g font-size="5.5" fill="#e8202a" text-anchor="middle">
      <text x="59" y="105">Category 1</text><text x="137" y="105">Category 2</text><text x="214" y="105">Category 3</text><text x="292" y="105">Category 4</text>
    </g>
  </svg>
  <p class="chart-outro">Lorem ipsum dolor sit amet, consectetur adipiscing elit. Vestibulum nec eros in dolor posuere interdum</p>
  <svg class="footer" viewBox="0 0 381 52" preserveAspectRatio="none"><path d="M0 24 Q190 10 381 14 L381 22 Q190 18 0 32 Z" fill="#333335"/><path d="M0 36 Q190 22 381 26 L381 52 L0 52 Z" fill="#e8202a"/></svg>
  <span class="url">www.rivoplex.com &nbsp;|&nbsp; 9</span>
</section>

<!-- 11 Contact -->
<section class="slide c2 r4">
  <div class="title-brand" style="top:33px">RIVOPLEX<span class="dot"></span></div>
  <svg class="footer" style="height:214px;top:0" viewBox="0 0 381 214" preserveAspectRatio="none">
    <path d="M0 82 Q190 72 381 88 L381 96 Q190 80 0 92 Z" fill="#333335"/>
    <path d="M0 96 Q190 84 381 100 L381 214 L0 214 Z" fill="#e8202a"/>
  </svg>
  <div class="squares"><span style="left:306px;top:98px;width:22px;height:22px"></span><span style="left:343px;top:120px;width:28px;height:28px"></span><span style="left:290px;top:132px;width:36px;height:36px"></span><span style="left:334px;top:163px;width:47px;height:47px"></span></div>
  <h3 class="contact-head">Contact Us:</h3>
  <ul class="contact-lines">
    <li>418 Harbor Point Drive, Suite 210</li>
    <li>Oceanside, CA 92054, USA</li>
    <li class="gap"><svg viewBox="0 0 10 10"><path d="M2 1 L4 3 L3 4.5 Q4.5 6.5 5.5 7 L7 6 L9 8 L7.5 9.5 Q2 8 0.5 2.5 Z" fill="#fff"/></svg>+1 (555) 014-2290</li>
    <li><svg viewBox="0 0 10 10"><rect x="0.5" y="2" width="9" height="6.5" fill="#fff"/><path d="M0.5 2 L5 6 L9.5 2" fill="none" stroke="#e8202a" stroke-width=".8"/></svg>contact@rivoplex.com</li>
    <li><svg viewBox="0 0 10 10"><circle cx="5" cy="5" r="4.3" fill="none" stroke="#fff" stroke-width=".9"/><path d="M0.7 5 H9.3 M5 0.7 V9.3" stroke="#fff" stroke-width=".7"/><ellipse cx="5" cy="5" rx="2" ry="4.3" fill="none" stroke="#fff" stroke-width=".7"/></svg>www.rivoplex.com</li>
  </ul>
</section>

<!-- 12 Thank You -->
<section class="slide c3 r4" style="background:var(--red)">
  <div class="squares"><span style="left:231px;top:10px;width:34px;height:34px"></span><span style="left:291px;top:58px;width:26px;height:26px"></span><span style="left:224px;top:76px;width:56px;height:56px"></span><span style="left:297px;top:122px;width:84px;height:84px"></span></div>
  <h2 class="thanks">Thank You!</h2>
</section>

</body>
</html>
```